Business cards for KORBEN Real Estate Properties LLC

We need a cool, original business card design for a company based in the Washington DC metropolitan area. We are a new energetic and passionate Real Estate Investing Company that invests in all types of real estate; commercial, residential, industrial etc.

Our company color is Red since it reflects action, energy and speed; it is assertive confident, energizing, exciting, powerful, passionate and determined. So we would like business card communicate those qualities to the audience.

Our audiences are investors that want to invest with us, real estate sellers, buyers, and tenants who lease from us.

Our logo is attached

```html
<!DOCTYPE html>
<html lang="en">
<head>
<meta charset="utf-8">
<title>KORBEN Real Estate Properties LLC — Business Cards</title>
<link rel="stylesheet" href="https://fonts.googleapis.com/css2?family=Arimo:wght@400;700&family=Open+Sans:wght@400;600;800&display=swap">
<style>
  :root {
    --backdrop: #9a9a9a;
    --card: #ffffff;
    --ink: #111111;
    --charcoal: #3b3b3d;
    --brand-red: #e0232b;
    --bar-grey: #a5a3a4;
    --soft-grey: #bdbdbd;
  }
  * { margin: 0; padding: 0; box-sizing: border-box; }
  html, body { width: 1200px; height: 960px; overflow: hidden; }
  body {
    background: var(--backdrop);
    position: relative;
    font-family: "Arimo", Arial, sans-serif;
  }
  .card {
    position: absolute;
    top: 130px;
    width: 400px;
    height: 700px;
    background: var(--card);
  }
  .card--front { left: 130px; }
  .card--back { left: 670px; }

  .brand-stripe {
    position: absolute;
    left: 50%;
    bottom: 22px;
    width: 118px;
    transform: translateX(-50%);
  }
  .brand-stripe span { display: block; }
  .brand-stripe .band-dark { height: 9px; background: var(--charcoal); }
  .brand-stripe .band-red { height: 13px; background: var(--brand-red); }
  .brand-stripe .band-grey { height: 7px; background: var(--soft-grey); }

  /* Front */
  .front-brand {
    position: absolute;
    left: 0; right: 0;
    top: 250px;
    text-align: center;
  }
  .front-brand .brand-mark {
    width: 56px; height: 56px;
    margin: 0 auto 34px;
    background: var(--brand-red);
  }
  .front-brand .brand-name {
    font-family: "Open Sans", Arial, sans-serif;
    font-weight: 800;
    font-size: 72px;
    letter-spacing: 2px;
    line-height: 1;
    color: var(--charcoal);
  }
  .front-brand .brand-tagline {
    margin-top: 10px;
    font-family: "Open Sans", Arial, sans-serif;
    font-weight: 400;
    font-size: 23px;
    color: var(--charcoal);
  }

  /* Back */
  .holder { position: absolute; left: 26px; top: 24px; }
  .holder .holder-name {
    font-size: 21px;
    font-variant: small-caps;
    color: var(--ink);
    letter-spacing: 0.5px;
  }
  .holder .holder-title {
    margin-top: 2px;
    margin-left: 3px;
    font-size: 21px;
    color: var(--brand-red);
  }
  .back-brand {
    position: absolute;
    left: 0; right: 0;
    top: 205px;
    display: flex;
    justify-content: center;
    align-items: center;
    gap: 12px;
  }
  .back-brand .brand-mark { width: 22px; height: 22px; background: var(--brand-red); }
  .back-brand .brand-name {
    font-family: "Open Sans", Arial, sans-serif;
    font-weight: 800;
    font-size: 32px;
    letter-spacing: 1px;
    color: var(--charcoal);
  }

  .contacts {
    position: absolute;
    left: 26px;
    right: 16px;
    top: 330px;
    list-style: none;
  }
  .contact {
    display: flex;
    align-items: stretch;
    margin-bottom: 24px;
  }
  .contact-icon {
    flex: 0 0 28px;
    height: 28px;
    margin-right: 8px;
    background: var(--ink);
    display: flex; align-items: center; justify-content: center;
  }
  .contact-icon svg { width: 20px; height: 20px; }
  .contact-text {
    flex: 1;
    background: var(--bar-grey);
    color: var(--ink);
    font-size: 16px;
    letter-spacing: 0.6px;
    padding: 4px 0 4px 26px;
    line-height: 20px;
  }
  .contact--address .contact-icon { height: 44px; align-self: center; background: var(--card); }
  .contact--address .contact-text { padding-top: 5px; padding-bottom: 5px; line-height: 22px; }
</style>
</head>
<body>

<section class="card card--front" aria-label="Business card front">
  <div class="front-brand">
    <div class="brand-mark"></div>
    <div class="brand-name">KORBEN</div>
    <div class="brand-tagline">REAL ESTATE PROPERTIES LLC</div>
  </div>
  <div class="brand-stripe"><span class="band-dark"></span><span class="band-red"></span><span class="band-grey"></span></div>
</section>

<section class="card card--back" aria-label="Business card back">
  <div class="holder">
    <div class="holder-name">Name Surname</div>
    <div class="holder-title">Director</div>
  </div>

  <div class="back-brand">
    <div class="brand-mark"></div>
    <div class="brand-name">KORBEN</div>
  </div>

  <ul class="contacts">
    <li class="contact">
      <span class="contact-icon">
        <svg viewBox="0 0 20 20" aria-hidden="true"><path d="M6 2 L8.5 6 L7 7.5 Q8.5 11.5 12.5 13 L14 11.5 L18 14 L16 17.5 Q8 17 3 8 Z" fill="#fff"/></svg>
      </span>
      <span class="contact-text">123 1233 123</span>
    </li>
    <li class="contact">
      <span class="contact-icon">
        <svg viewBox="0 0 20 20" aria-hidden="true"><rect x="2" y="4.5" width="16" height="11" fill="none" stroke="#fff" stroke-width="1.5"/><path d="M2 4.5 L10 11 L18 4.5" fill="none" stroke="#fff" stroke-width="1.5"/></svg>
      </span>
      <span class="contact-text">info@korbenrealestate.com</span>
    </li>
    <li class="contact">
      <span class="contact-icon">
        <svg viewBox="0 0 20 20" aria-hidden="true" fill="none" stroke="#fff" stroke-width="1.3"><circle cx="10" cy="10" r="8"/><ellipse cx="10" cy="10" rx="3.5" ry="8"/><path d="M2 10 H18 M3.5 6 H16.5 M3.5 14 H16.5"/></svg>
      </span>
      <span class="contact-text">www.korbenrealestate.com</span>
    </li>
    <li class="contact contact--address">
      <span class="contact-icon">
        <svg viewBox="0 0 20 20" aria-hidden="true"><path d="M1 9 L10 2 L19 9" fill="none" stroke="#111" stroke-width="1.8"/><rect x="4" y="9" width="12" height="10" fill="#111"/><rect x="6" y="11" width="3" height="3" fill="#fff"/><rect x="11" y="11" width="3" height="3" fill="#fff"/><rect x="8.5" y="15" width="3" height="4" fill="#fff"/></svg>
      </span>
      <span class="contact-text">Address line 1<br>Address line 2.</span>
    </li>
  </ul>

  <div class="brand-stripe"><span class="band-dark"></span><span class="band-red"></span><span class="band-grey"></span></div>
</section>

</body>
</html>
```